Packaging Design Project

Hi,

We are an small SME active in the hotels industry.
We deliver guest amenities.

We are thinking to create a our first neutral range for accessories.
This consists of a box (94mm/75mm/75mm) in which accessories will be stored.
Here below, you will find an editable pdf with the dimensions of the box.

This is for a neutral range supposed to fit in diverse kind of room, please take this into account : no vivid colors, you can imagine logo and/or colors as far as it remains discrete.

The box should be mostly white. You can imagine logo, forms, frames ... as fas as more than 60% of the box is white.

We will be very reactive to give you feedback. In the same time, you can propose a name for this neutral range.

In order to know the kind of name we like, our other range (not accessories) are called : Brio, Calm, Pure Leaf, Harmony.

For info, a range is composed by : soap, shower gel, body lotion...
the accessories of a range is composed by : shower cap, shoe sponge, sewing kit ...

Thanks in advance for your work !

Target Market(s)

it's a B2B hotels environment, but our client range from 1* to 5*

Industry/Entity Type

Industry

Requirements
Must have
• You have to respect the scale of the box provided in the file below.
Somewhere should appear our website : www.tolvan.be but in a very discrete way.

The design should be in black & white or gray & white
Nice to have
• a small discrete logo somewhere, but this is not mandatory
Should not have
• a lot of colors, a design having a too strong identity. this design is supposed to fit with the design of the hotel, whatever it is.

```html
<!DOCTYPE html>
<html lang="en">
<head>
<meta charset="utf-8">
<title>hush – accessories box</title>
<link rel="stylesheet" href="https://fonts.googleapis.com/css2?family=Bodoni+Moda:wght@600&family=Ultra&display=swap">
<style>
  :root {
    --board-light: #ffffff;
    --board-edge: #c9c9c9;
    --box-white: #ffffff;
    --ink: #111111;
    --brush-dark: #151414;
    --brush-mid: #2f2d2c;
    --brush-soft: #3e3b39;
    --label-ink: #0d0d0d;
    --name-ink: #f2f2f2;
  }
  * { box-sizing: border-box; margin: 0; padding: 0; }
  html, body { width: 1200px; height: 920px; overflow: hidden; }
  body {
    position: relative;
    background: radial-gradient(ellipse at 50% 45%, var(--board-light) 0%, #ededed 55%, var(--board-edge) 100%);
    font-family: "Bodoni Moda", serif;
  }
  .panel-label {
    position: absolute;
    font-family: "Ultra", serif;
    font-weight: 400;
    font-size: 38px;
    line-height: 1;
    color: var(--label-ink);
    white-space: nowrap;
  }
  .panel-label--top { left: 136px; top: 230px; }
  .panel-label--inner { left: 818px; top: 646px; }

  .box-face {
    position: absolute;
    box-shadow: 0 4px 14px rgba(0,0,0,0.35);
  }
  .cover-top {
    left: 400px; top: 50px; width: 396px; height: 394px;
    background: var(--box-white);
  }
  .cover-top__disc {
    position: absolute;
    left: 72px; top: 72px; width: 252px; height: 252px;
    border-radius: 50%;
    background: radial-gradient(circle at 30% 65%, var(--brush-soft) 0%, var(--brush-dark) 45%, var(--ink) 100%);
  }
  .inner-cover {
    left: 400px; top: 456px; width: 408px; height: 416px;
    background: radial-gradient(ellipse at 15% 30%, var(--brush-mid) 0%, var(--brush-dark) 40%, var(--ink) 75%, var(--brush-mid) 100%);
  }
  .range-name {
    position: absolute;
    left: 0; right: 0;
    text-align: center;
    color: var(--name-ink);
    font-weight: 600;
    line-height: 1;
  }
  .cover-top .range-name { top: 178px; font-size: 34px; }
  .inner-cover .range-name { top: 182px; font-size: 44px; }
  .range-tagline {
    position: absolute;
    left: 0; right: 0; top: 248px;
    text-align: center;
    color: var(--name-ink);
    font-size: 10px;
    font-weight: 600;
    line-height: 1;
    letter-spacing: 0.3px;
  }
</style>
</head>
<body>
  <div class="panel-label panel-label--top">cover top</div>
  <div class="panel-label panel-label--inner">inner cover</div>

  <section class="box-face cover-top">
    <div class="cover-top__disc" role="img" aria-label="Black disc with soft grey brush-stroke texture"></div>
    <p class="range-name">hush</p>
  </section>

  <section class="box-face inner-cover" role="img" aria-label="Black panel with grey sweeping brush-stroke texture">
    <p class="range-name">hush</p>
    <p class="range-tagline">your basic accessories</p>
  </section>
</body>
</html>
```